Orlow Wellness Group Website

Need a informative, detailed and functional website for a medical cannabis clinic website

check out www.tesmorahealthcare.com as competition - want better site than they have

Target Market(s)

Patients

Industry/Entity Type

Health Care

Number of Pages Required

1 page

Font styles to use
Sans Serif

Colors
cadf82
abd036
9bcb3b
3276b5
33a6d7
0392cd
f68d4e

Requirements
Must have
• Clean / Informative
• Will add additional educational content on opioid reduction
Nice to have
• like the white contrast with black/slate dividers. Green logo looks good on slate
• Check documents for ppt regarding website ideas
Should not have
• too many words

```html
<!DOCTYPE html>
<html lang="en">
<head>
<meta charset="utf-8">
<title>Arkansas Orlow Wellness Group</title>
<link href="https://fonts.googleapis.com/css2?family=Lato:wght@400;700;900&display=swap" rel="stylesheet">
<style>
:root{
  --green:#9bcb3b;
  --green-dark:#5ea52a;
  --green-light:#cadf82;
  --orange:#f68d4e;
  --blue:#0392cd;
  --grey-band:#ececec;
  --text:#444;
  --muted:#777;
  --footer:#242424;
  --footer-bar:#1b1b1b;
  --white:#fff;
}
*{box-sizing:border-box;margin:0;padding:0}
html,body{width:1200px;height:3056px;overflow:hidden}
body{font-family:'Lato',Arial,sans-serif;color:var(--text);background:var(--white);position:relative}
.abs{position:absolute}

/* header */
.site-header{position:absolute;top:0;left:0;width:1200px;height:96px;background:var(--white)}
.brand{position:absolute;left:163px;top:18px;display:flex;align-items:center;gap:12px}
.brand-dot{width:56px;height:56px;border-radius:50%;background:var(--green);flex:none}
.brand-name{color:var(--green-dark);font-weight:700;font-size:14px;line-height:17px;letter-spacing:3px;text-transform:uppercase;width:210px}
.header-phone{position:absolute;right:204px;top:10px;color:var(--green-dark);font-weight:700;font-size:19px;display:flex;align-items:center;gap:6px}
.main-nav{position:absolute;left:437px;top:50px;display:flex;gap:25px;font-size:15px;font-weight:700;color:#333}

/* hero */
.hero{position:absolute;top:96px;left:0;width:1200px;height:546px;
  background:linear-gradient(180deg,#f6b24a 0%,#e5862f 22%,#8a7a3a 50%,#4f6a26 75%,#3f5a1d 100%)}
.hero-arrow{position:absolute;top:200px}
.hero-copy{position:absolute;left:121px;top:104px;width:500px;text-align:center;color:var(--white)}
.hero-mark{width:38px;height:38px;border-radius:50%;border:3px solid var(--white);margin:0 auto 12px}
.hero-kicker{font-size:26px;font-weight:400;line-height:30px}
.hero-title{font-size:42px;font-weight:900;line-height:44px}
.hero-title span{font-size:34px;display:block;line-height:40px}
.btn{display:inline-block;border-radius:30px;font-weight:700;text-transform:uppercase;text-align:center}
.btn-hero{position:absolute;left:253px;top:288px;width:240px;height:53px;line-height:53px;background:var(--green);color:var(--white);font-size:18px}

/* feature cards */
.feature{position:absolute;top:574px;width:276px;height:198px;color:var(--white);text-align:center;box-shadow:0 4px 8px rgba(0,0,0,.2)}
.feature-icon{position:absolute;left:94px;top:-58px;width:88px;height:88px;border-radius:50%;display:flex;align-items:center;justify-content:center}
.feature h3{margin-top:38px;font-size:19px;font-weight:900;line-height:22px;text-transform:uppercase}
.feature p{font-size:12.5px;line-height:18px;margin:6px 22px 0}
.btn-outline-white{margin-top:12px;width:124px;height:36px;line-height:32px;border:2px solid var(--white);color:var(--white);font-size:12px}
.feature-green{left:161px;background:var(--green)}
.feature-green .feature-icon{background:var(--green)}
.feature-orange{left:460px;background:var(--orange)}
.feature-orange .feature-icon{background:var(--orange)}
.feature-blue{left:757px;background:var(--blue)}
.feature-blue .feature-icon{background:var(--blue)}

/* about */
.about-visual{position:absolute;left:175px;top:845px;width:365px;height:330px;border-radius:50%;
  background:radial-gradient(circle,#5f9fcf 0%,#5c8a3c 55%,#2f4a1e 100%)}
.about-copy{position:absolute;left:589px;top:876px;width:480px}
.about-copy h2{font-size:32px;font-weight:700;color:var(--green-dark);line-height:36px}
.about-copy h2 span{display:block;font-size:26px;color:var(--green)}
.about-copy p{font-size:18px;line-height:28px;color:#555;margin-top:18px}
.about-copy p+p{margin-top:14px}
.btn-outline-green{margin-top:28px;width:158px;height:48px;line-height:44px;border:2px solid var(--green);color:var(--green);font-size:15px}

/* steps */
.steps{position:absolute;top:1293px;left:0;width:1200px;height:524px;background:var(--grey-band)}
.steps-notch{position:absolute;left:556px;top:-2px;width:0;height:0;border-left:44px solid transparent;border-right:44px solid transparent;border-top:30px solid var(--white)}
.steps h2{position:absolute;top:72px;left:0;width:1200px;text-align:center;font-size:25px;font-weight:700;color:#333;line-height:33px;text-transform:uppercase}
.step{position:absolute;top:182px;width:260px;text-align:center}
.step-circle{width:130px;height:130px;border-radius:50%;margin:0 auto;display:flex;align-items:center;justify-content:center}
.step h3{margin-top:28px;font-size:15px;font-weight:900;color:#333;line-height:19px;text-transform:uppercase}
.step p{margin-top:14px;font-size:14px;line-height:19px;color:var(--muted)}
.step-arrow{position:absolute;top:196px}

/* service cards */
.service{position:absolute;top:1874px;width:276px;height:380px;border:1px solid #ccc;background:var(--white);text-align:center}
.service-photo{height:180px}
.service h3{margin-top:20px;font-size:19px;font-weight:900;color:var(--green);line-height:22px;text-transform:uppercase}
.service p{margin:10px 26px 0;font-size:13px;line-height:19px;color:#555}
.btn-green{position:absolute;left:75px;bottom:18px;width:124px;height:38px;line-height:38px;background:var(--green);color:var(--white);font-size:12px}

/* cta band */
.newsletter{position:absolute;top:2336px;left:0;width:597px;height:318px;background:var(--green);color:var(--white)}
.help{position:absolute;top:2336px;left:597px;width:603px;height:318px;background:var(--orange);color:var(--white)}
.band-title{position:absolute;top:60px;font-size:27px;font-weight:700;text-transform:uppercase}
.band-text{position:absolute;top:104px;font-size:14px;line-height:19px;width:420px}
.email-field{position:absolute;left:167px;top:168px;width:388px;height:50px;border-radius:26px;background:var(--white);color:#555;font-size:15px;line-height:50px;padding-left:28px}
.email-go{position:absolute;right:12px;top:11px;width:30px;height:30px;border-radius:50%;background:var(--green);display:flex;align-items:center;justify-content:center}
.help-phone{position:absolute;left:55px;top:164px;font-size:26px;font-weight:700;display:flex;align-items:center;gap:8px}

/* footer */
.site-footer{position:absolute;top:2654px;left:0;width:1200px;height:340px;background:var(--footer);color:#ccc}
.footer-brand{position:absolute;left:160px;top:68px;display:flex;align-items:center;gap:12px}
.footer-brand .brand-name{color:var(--green);width:170px}
.footer-about{position:absolute;left:166px;top:165px;width:190px;font-size:12px;line-height:17px;color:#bbb}
.footer-col h4{font-size:17px;font-weight:700;color:var(--white);text-transform:uppercase}
.footer-col ul{list-style:none;margin-top:20px}
.footer-col li{font-size:14px;line-height:25px;color:#bbb}
.social{display:flex;gap:20px;margin-top:18px}
.social span{width:16px;height:16px;border-radius:50%;background:#ddd;display:block}
.field{width:278px;height:36px;background:#3b3b3b;color:#aaa;font-size:14px;line-height:36px;padding-left:12px;margin-top:10px}
.btn-submit{margin-top:20px;width:126px;height:38px;line-height:38px;background:var(--green);color:var(--white);font-size:15px}
.footer-bar{position:absolute;top:2994px;left:0;width:1200px;height:62px;background:var(--footer-bar);color:#999;font-size:13px;text-align:center;line-height:62px}
</style>
</head>
<body>

<header class="site-header">
  <div class="brand"><span class="brand-dot"></span><span class="brand-name">Arkansas Orlow Wellness Group</span></div>
  <div class="header-phone">
    <svg width="18" height="18" viewBox="0 0 24 24"><path fill="#5ea52a" d="M6.6 10.8a15 15 0 0 0 6.6 6.6l2.2-2.2a1 1 0 0 1 1-.25 11.4 11.4 0 0 0 3.6.57 1 1 0 0 1 1 1V20a1 1 0 0 1-1 1A17 17 0 0 1 3 4a1 1 0 0 1 1-1h3.5a1 1 0 0 1 1 1c0 1.25.2 2.45.57 3.57a1 1 0 0 1-.25 1z"/></svg>
    855-555-0142
  </div>
  <nav class="main-nav"><span>HOME</span><span>ABOUT US</span><span>SERVICES</span><span>FAQ</span><span>NEWS</span><span>APPOINTMENT</span><span>CONTACT</span></nav>
</header>

<section class="hero" role="img" aria-label="Woman stretching her arms in a sunlit green field at sunset">
  <svg class="hero-arrow" style="left:80px" width="34" height="64" viewBox="0 0 34 64"><path d="M30 4 4 32l26 28" fill="none" stroke="#fff" stroke-width="3"/></svg>
  <svg class="hero-arrow" style="right:80px" width="34" height="64" viewBox="0 0 34 64"><path d="M4 4l26 28L4 60" fill="none" stroke="#fff" stroke-width="3"/></svg>
  <div class="hero-copy">
    <div class="hero-mark"></div>
    <div class="hero-kicker">WELCOME TO</div>
    <div class="hero-title">ARKANSAS ORLOW<span>WELLNESS GROUP</span></div>
  </div>
  <span class="btn btn-hero">Book Appointment</span>
</section>

<article class="feature feature-green">
  <div class="feature-icon"><svg width="44" height="44" viewBox="0 0 44 44"><circle cx="22" cy="22" r="18" fill="none" stroke="#fff" stroke-width="3"/><path d="M13 22l6 6 12-12" fill="none" stroke="#fff" stroke-width="3"/></svg></div>
  <h3>100% Risk Free</h3>
  <p>Lorem ipsum dolor sit amet consecte tuer adipiscing elit Nam cursus Morbi ut mi Nullam enim leo</p>
  <span class="btn btn-outline-white">Read More</span>
</article>
<article class="feature feature-orange">
  <div class="feature-icon"><svg width="44" height="44" viewBox="0 0 44 44"><path d="M24 6h14v14L20 38 6 24z" fill="none" stroke="#fff" stroke-width="3"/><circle cx="31" cy="13" r="3" fill="#fff"/></svg></div>
  <h3>Inexpensive</h3>
  <p>Lorem ipsum dolor sit amet consecte tuer adipiscing elit Nam cursus Morbi ut mi Nullam enim leo</p>
  <span class="btn btn-outline-white">Read More</span>
</article>
<article class="feature feature-blue">
  <div class="feature-icon"><svg width="48" height="44" viewBox="0 0 48 44"><circle cx="18" cy="18" r="14" fill="none" stroke="#fff" stroke-width="3"/><text x="18" y="25" fill="#fff" font-size="18" font-weight="700" text-anchor="middle" font-family="Lato,sans-serif">?</text><rect x="26" y="24" width="18" height="14" rx="3" fill="none" stroke="#fff" stroke-width="3"/></svg></div>
  <h3>FAQ</h3>
  <p>Lorem ipsum dolor sit amet consecte tuer adipiscing elit Nam cursus Morbi ut mi Nullam enim leo</p>
  <span class="btn btn-outline-white">Read More</span>
</article>

<div class="about-visual" role="img" aria-label="Leaf-shaped frame filled with a photo of palm trees and blue sky"></div>
<section class="about-copy">
  <h2>ABOUT ARKANSAS ORLOW<span>WELLNESS GROUP</span></h2>
  <p>Pellentesque faucibus Ut accumsan ultricies elit Maecenas at justo id velit placerat molestie Donec dictum lectus non odio Cras a ante vitae enim iaculis aliquam</p>
  <p>Mauris nunc quam venenatis nec euismod sit amet egestas placerat est Pellentesque habitant morbi tristique</p>
  <span class="btn btn-outline-green">Read More</span>
</section>

<section class="steps">
  <div class="steps-notch"></div>
  <h2>3 Steps to Get Your Arkansas<br>Marijuna Card</h2>
  <div class="step" style="left:182px">
    <div class="step-circle" style="background:var(--green-light)" role="img" aria-label="Doctor icon"></div>
    <h3>Donec Convallis Pede<br>Venenatis Nib</h3>
    <p>Mauris nunc quam venenatis<br>nec euismod sit amet egestas<br>placerat est Pelle</p>
  </div>
  <svg class="step-arrow" style="left:396px" width="104" height="40" viewBox="0 0 104 40"><path d="M4 34C30 4 70 4 96 30" fill="none" stroke="#888" stroke-width="4"/><path d="M86 30h12V18" fill="none" stroke="#888" stroke-width="4"/></svg>
  <div class="step" style="left:467px">
    <div class="step-circle" style="background:var(--green)"><svg width="60" height="70" viewBox="0 0 60 70"><rect x="6" y="4" width="48" height="62" rx="3" fill="none" stroke="#fff" stroke-width="3"/><path d="M16 18h28M16 30h28M16 42h28M16 54h18" stroke="#fff" stroke-width="3"/></svg></div>
    <h3>Fusce Tellus Sed Metus<br>Augue Convallis</h3>
    <p>Mauris nunc quam venenatis<br>nec euismod sit amet egestas<br>placerat est Pelle</p>
  </div>
  <svg class="step-arrow" style="left:692px" width="104" height="40" viewBox="0 0 104 40"><path d="M4 34C30 4 70 4 96 30" fill="none" stroke="#888" stroke-width="4"/><path d="M86 30h12V18" fill="none" stroke="#888" stroke-width="4"/></svg>
  <div class="step" style="left:752px">
    <div class="step-circle" style="background:var(--orange)"><svg width="64" height="64" viewBox="0 0 64 64"><rect x="6" y="10" width="52" height="48" rx="4" fill="none" stroke="#fff" stroke-width="3"/><path d="M6 22h52M18 4v12M46 4v12" stroke="#fff" stroke-width="3"/><g fill="#fff"><circle cx="18" cy="32" r="3"/><circle cx="30" cy="32" r="3"/><circle cx="42" cy="32" r="3"/><circle cx="18" cy="44" r="3"/><circle cx="30" cy="44" r="3"/><circle cx="42" cy="44" r="3"/></g></svg></div>
    <h3>Praesent Vitae<br>Lacus Ut Velit</h3>
    <p>Mauris nunc quam venenatis<br>nec euismod sit amet egestas<br>placerat est Pelle</p>
  </div>
</section>

<article class="service" style="left:161px">
  <div class="service-photo" role="img" aria-label="Close-up of green cannabis leaves" style="background:linear-gradient(135deg,#2f5a1c,#6c9a3a,#254615)"></div>
  <h3>Convenience</h3>
  <p>Mauris nunc quam venenatis nec euismod sit amet egestas placerat est Pellentesque habitant morbi tristique senectus et netus et</p>
  <span class="btn btn-green">Read More</span>
</article>
<article class="service" style="left:460px">
  <div class="service-photo" role="img" aria-label="Cannabis plant glowing in warm sunlight" style="background:linear-gradient(135deg,#e8b030,#9a8a25,#4c5e18)"></div>
  <h3>No Qualification?<br>No Fee</h3>
  <p>Cras a ante vitae enim iaculis aliquam Mauris nunc quam venenatis nec euismod sit amet egestas</p>
  <span class="btn btn-green">Read More</span>
</article>
<article class="service" style="left:756px">
  <div class="service-photo" role="img" aria-label="Physician in a white coat holding a clipboard in a cannabis field" style="background:linear-gradient(135deg,#3e6b27,#7aa152,#3a5e22)"></div>
  <h3>Qualifies<br>Physicians</h3>
  <p>Cras a ante vitae enim iaculis aliquam Mauris nunc quam venenatis nec euismod sit amet egestas</p>
  <span class="btn btn-green">Read More</span>
</article>

<section class="newsletter">
  <h2 class="band-title" style="left:170px">Newsletter Sign Up</h2>
  <p class="band-text" style="left:170px">Cras a ante vitae enim iaculis aliquam Mauris nunc quam venenatis nec euismod sit amet egestas</p>
  <div class="email-field">Email address
    <span class="email-go"><svg width="14" height="14" viewBox="0 0 14 14"><path d="M5 2l5 5-5 5" fill="none" stroke="#fff" stroke-width="2.5"/></svg></span>
  </div>
</section>
<section class="help">
  <h2 class="band-title" style="left:55px">Need Help?</h2>
  <p class="band-text" style="left:55px">Cras a ante vitae enim iaculis aliquam Mauris nunc quam venenatis nec euismod sit amet egestas</p>
  <div class="help-phone">
    <svg width="22" height="22" viewBox="0 0 24 24"><path fill="#fff" d="M6.6 10.8a15 15 0 0 0 6.6 6.6l2.2-2.2a1 1 0 0 1 1-.25 11.4 11.4 0 0 0 3.6.57 1 1 0 0 1 1 1V20a1 1 0 0 1-1 1A17 17 0 0 1 3 4a1 1 0 0 1 1-1h3.5a1 1 0 0 1 1 1c0 1.25.2 2.45.57 3.57a1 1 0 0 1-.25 1z"/></svg>
    855-555-0142
  </div>
</section>

<footer class="site-footer">
  <div class="footer-brand"><span class="brand-dot"></span><span class="brand-name">Arkansas Orlow Wellness Group</span></div>
  <p class="footer-about">Maecenas aliquet velit vel turpis Mauris neque metus malesuada nec ultricies sit amet port</p>
  <div class="footer-col abs" style="left:404px;top:66px">
    <h4>Quick Links</h4>
    <ul><li>About Us</li><li>Our Services</li><li>News</li><li>How it Works</li><li>Contact Us</li></ul>
  </div>
  <div class="footer-col abs" style="left:560px;top:66px">
    <h4>Contact Us</h4>
    <ul><li>48 Linden Row Suite 3</li><li>Little Rock AR 72201</li><li>501.555.0187</li><li>hello@orlowwellness.com</li></ul>
    <div class="social"><span></span><span></span><span></span></div>
  </div>
  <div class="footer-col abs" style="left:764px;top:62px">
    <h4>Contact Form</h4>
    <div class="field" style="margin-top:18px">Name</div>
    <div class="field">Phone</div>
    <div class="field">Email</div>
    <span class="btn btn-submit">Submit</span>
  </div>
</footer>
<div class="footer-bar">© 2019 Orlow Wellness Group &nbsp;All right reserved</div>

</body>
</html>
```